CONTEMPORARY Canva Art Design for Christians

I need a canvas art design on Christianity. The design must be in 3 SIMPLE dimensions: 12x 18 inches / 28 x 24 inches / 30 x 40 inches
The design must be accompanied by christian quote.
The christian quote can be "As For Me And My House We Will Serve The Lord (Joshua 24:15)" or any other quote that is good for display in a christian home.

I DON'T WANT THE TRADITIONAL CHRISTIAN DESIGN.. I WANT COLOURFUL, MEANINGFUL and CONTEMPORARY, MODERN DESIGN. And stay away from the scary image of Jesus in dark background, it only makes the home more scary not holy!

Target Market(s)

Christians

Colors

Designer to choose colors to be used in the design.

Requirements
Must have
• A graphic design and a christian quote that is powerful and edifies the soul. Great for display at home. Great use of colours to enhance the message.
Nice to have
• I wish to see great unique design with strong use of colours, images to enhance the scripture. It must glorify Jesus.
Should not have
• Should not be dull.

```html
<!DOCTYPE html>
<html lang="en">
<head>
<meta charset="utf-8">
<title>As For Me And My House – Joshua 24:15 Canvas Art</title>
<link rel="stylesheet" href="https://fonts.googleapis.com/css2?family=Roboto+Condensed:wght@300;400&display=swap">
<style>
  :root {
    --page-bg: #e9eaec;
    --frame-edge: #1a1a1a;
    --sky-glow: #f4f8fe;
    --sky-pale: #c4dbf8;
    --sky-mid: #5c9bea;
    --sky-deep: #1a4fc4;
    --sky-night: #0a2f9e;
    --spirit-white: #fbfcff;
    --verse-ink: #111111;
  }
  html, body {
    margin: 0;
    padding: 0;
    width: 1200px;
    height: 1200px;
    overflow: hidden;
    background: var(--page-bg);
  }
  .canvas-print {
    position: absolute;
    left: 30px;
    top: 219px;
    width: 1140px;
    height: 762px;
    box-sizing: border-box;
    border: 2px solid var(--frame-edge);
    overflow: hidden;
  }
  .heaven-scene {
    position: absolute;
    inset: 0;
    background:
      radial-gradient(ellipse 45% 40% at 53% 22%, var(--sky-glow) 0%, rgba(220,234,252,0.9) 40%, rgba(150,190,240,0.4) 75%, rgba(150,190,240,0) 100%),
      radial-gradient(ellipse 30% 18% at 18% 62%, rgba(230,240,255,0.5) 0%, rgba(230,240,255,0) 100%),
      radial-gradient(ellipse 28% 16% at 88% 58%, rgba(230,240,255,0.5) 0%, rgba(230,240,255,0) 100%),
      linear-gradient(180deg, var(--sky-mid) 0%, var(--sky-deep) 72%, var(--sky-night) 100%);
  }
  .dove-and-cross {
    position: absolute;
    left: 378px;
    top: 62px;
    width: 431px;
    height: 260px;
    border-radius: 48% 48% 46% 46%;
    background: radial-gradient(ellipse 60% 60% at 50% 45%, var(--spirit-white) 0%, rgba(255,255,255,0.95) 55%, rgba(236,243,253,0.85) 100%);
    box-shadow: 0 0 40px 18px rgba(255,255,255,0.75);
  }
  .verse {
    position: absolute;
    left: 0;
    right: 0;
    top: 366px;
    margin: 0;
    padding-left: 74px;
    text-align: center;
    font-family: "Roboto Condensed", "Arial Narrow", sans-serif;
    color: var(--verse-ink);
  }
  .verse-line {
    display: block;
    font-weight: 300;
    font-size: 67px;
    line-height: 79px;
    letter-spacing: -0.8px;
    text-transform: uppercase;
  }
  .verse-reference {
    display: block;
    margin-top: -6px;
    font-style: normal;
    font-weight: 300;
    font-size: 33px;
    line-height: 40px;
  }
</style>
</head>
<body>
  <main class="canvas-print">
    <div class="heaven-scene" role="img" aria-label="Bright blue sky with radiant light rays and white clouds"></div>
    <div class="dove-and-cross" role="img" aria-label="White dove with outstretched wings in front of a glowing white cross"></div>
    <blockquote class="verse">
      <span class="verse-line">As for me and</span>
      <span class="verse-line">my house</span>
      <span class="verse-line">we will serve</span>
      <span class="verse-line">the Lord</span>
      <cite class="verse-reference">(JOSHUA 24:15)</cite>
    </blockquote>
  </main>
</body>
</html>
```